TRUCK WASH OUTDOOR DRIVE THROUGH MENU CONTEST

WE NEED A DRIVE THROUGH MENU WITH OUR SERVICES AND PRICES. I HAVE ATTACHED A FEW EXAMPLES THAT I STARTED.

I WANT THIS TO BE EYE CATCHING WITH BRIGHT COLORS

Target Market(s)

TRUCK WASH AND DETAIL SHOP, TRANSPORTATION.

Requirements
Must have
• INCORPORATE MY LOGO INTO THE SIGN.
• FINAL PROJECT MUST BE IN .AI FORMAT.
• COMPANY COLORS ARE RED AND BLUE

```html
<!DOCTYPE html>
<html lang="en">
<head>
<meta charset="utf-8">
<title>Rigline Wash – Wash Prices</title>
<link rel="stylesheet" href="https://fonts.googleapis.com/css2?family=Fredoka:wght@500;600;700&family=Arimo:wght@400&display=swap">
<style>
  :root {
    --ink: #000000;
    --paper: #ffffff;
    --brand-red: #e8232f;
    --brand-blue: #2fa8e0;
    --navy: #1b3a84;
    --sky-light: #dcefff;
    --sky: #8cc8f0;
    --sky-deep: #1f7cc9;
    --pill-border: #2e6cc0;
    --platinum: #b8a6d8;
    --platinum-fold: #8d7bb0;
    --gold: #e6b324;
    --gold-fold: #b58814;
    --silver: #cfcfcf;
    --silver-fold: #9a9a9a;
    --express: #56bde9;
    --express-fold: #2f8fc0;
    --text-muted: #1e1e2a;
  }
  * { margin: 0; padding: 0; box-sizing: border-box; }
  html, body { width: 848px; height: 1200px; overflow: hidden; background: var(--paper); }
  .menu-board {
    position: relative; width: 848px; height: 1200px; overflow: hidden;
    background: linear-gradient(180deg, var(--sky-light) 40%, var(--sky) 75%, var(--sky-deep) 100%);
    font-family: 'Arimo', Arial, sans-serif;
  }
  .top-rule { position: absolute; left: 0; top: 0; width: 100%; height: 20px; background: var(--ink); }
  .brand-header {
    position: absolute; left: 0; top: 20px; width: 100%; height: 264px; background: var(--paper);
    display: flex; align-items: center; justify-content: center; gap: 22px;
  }
  .brand-dot { width: 70px; height: 70px; border-radius: 50%; background: var(--brand-blue); }
  .brand-name {
    font-family: 'Fredoka', sans-serif; font-weight: 700; font-size: 86px;
    color: var(--brand-red); letter-spacing: 1px;
  }
  .bubble-band {
    position: absolute; left: 0; top: 284px; width: 100%; height: 124px;
    background: linear-gradient(180deg, #6fb6e8 0%, #bfe2fb 50%, #7ec0ee 100%);
  }
  .vehicle-title {
    position: absolute; left: 30px; top: 309px; width: 788px; height: 76px;
    border: 5px solid var(--pill-border); border-radius: 40px;
    background: rgba(255,255,255,0.35);
    display: flex; align-items: center; justify-content: center;
    font-family: 'Fredoka', sans-serif; font-weight: 700; font-size: 45px;
    color: var(--brand-red);
    -webkit-text-stroke: 8px var(--paper); paint-order: stroke fill;
    text-shadow: 0 0 2px var(--pill-border);
  }
  .section-bar {
    position: absolute; left: 0; top: 408px; width: 100%; height: 74px; background: var(--ink);
    display: flex; align-items: center; padding-left: 43px;
    font-family: 'Fredoka', sans-serif; font-weight: 600; font-size: 38px; color: var(--paper);
  }
  .price-panel {
    position: absolute; left: 42px; top: 482px; width: 766px; height: 686px;
    background:
      repeating-linear-gradient(0deg, rgba(120,160,210,0.25) 0 1px, transparent 1px 14px),
      repeating-linear-gradient(90deg, rgba(120,160,210,0.25) 0 1px, transparent 1px 14px),
      linear-gradient(180deg, #f3f8ff 0%, #d8e6fb 100%);
  }
  .tier { position: absolute; left: 0; width: 848px; height: 140px; }
  .tier-label, .tier-price { position: absolute; top: 0; width: 216px; height: 140px; }
  .tier-label { left: 16px; }
  .tier-price { left: 634px; }
  .tier svg { position: absolute; left: 0; top: 0; }
  .tier-label span, .tier-price span {
    position: absolute; top: 0; height: 86px; width: 100%;
    display: flex; align-items: center; justify-content: center;
    font-family: 'Fredoka', sans-serif; font-weight: 600; color: var(--navy);
  }
  .tier-label span { font-size: 33px; padding-right: 14px; }
  .tier-price span { font-size: 56px; font-weight: 700; padding-left: 8px; }
  .tier-services {
    position: absolute; left: 232px; top: 4px; width: 390px; text-align: center;
    font-size: 22.5px; line-height: 25px; color: var(--text-muted);
  }
  .tier-services.short { top: 22px; }
  .bullet { color: var(--navy); }
  .contact-note {
    position: absolute; left: 0; top: 1082px; width: 100%; text-align: center;
    font-family: 'Fredoka', sans-serif; font-weight: 600; font-size: 26px; line-height: 30px;
    color: var(--navy);
  }
</style>
</head>
<body>
<main class="menu-board">
  <div class="top-rule"></div>

  <header class="brand-header">
    <div class="brand-dot"></div>
    <div class="brand-name">Rigline Wash</div>
  </header>

  <div class="bubble-band" role="img" aria-label="Water bubble texture band"></div>
  <h1 class="vehicle-title">Standard Tractor &amp; Trailer (53’)</h1>

  <h2 class="section-bar">Wash Prices</h2>

  <div class="price-panel" role="img" aria-label="Light grid backdrop with water droplets"></div>

  <section class="tier" style="top:522px">
    <div class="tier-label">
      <svg width="216" height="140"><path d="M0 40 V130 Q2 100 34 94 V40 Z" fill="var(--platinum-fold)"/><rect x="0" y="0" width="216" height="86" rx="40" fill="var(--platinum)"/></svg>
      <span>PLATINUM</span>
    </div>
    <p class="tier-services">PreSoak <span class="bullet">●</span> Undercarriage rinse<br><span class="bullet">●</span> Soap and Scrub <span class="bullet">●</span> Tire Shine<br><span class="bullet">●</span> Platinum Protection</p>
    <div class="tier-price">
      <svg width="216" height="140"><path d="M216 40 V130 Q214 100 182 94 V40 Z" fill="var(--platinum-fold)"/><rect x="0" y="0" width="216" height="86" rx="40" fill="var(--platinum)"/></svg>
      <span>$130</span>
    </div>
  </section>

  <section class="tier" style="top:674px">
    <div class="tier-label">
      <svg width="216" height="140"><path d="M0 40 V130 Q2 100 34 94 V40 Z" fill="var(--gold-fold)"/><rect x="0" y="0" width="216" height="86" rx="40" fill="var(--gold)"/></svg>
      <span>GOLD</span>
    </div>
    <p class="tier-services">PreSoak <span class="bullet">●</span> Undercarriage rinse<br><span class="bullet">●</span> Soap and Scrub <span class="bullet">●</span> Tire Shine<br><span class="bullet">●</span> Wet X Polish</p>
    <div class="tier-price">
      <svg width="216" height="140"><path d="M216 40 V130 Q214 100 182 94 V40 Z" fill="var(--gold-fold)"/><rect x="0" y="0" width="216" height="86" rx="40" fill="var(--gold)"/></svg>
      <span>$120</span>
    </div>
  </section>

  <section class="tier" style="top:823px">
    <div class="tier-label">
      <svg width="216" height="140"><path d="M0 40 V130 Q2 100 34 94 V40 Z" fill="var(--silver-fold)"/><rect x="0" y="0" width="216" height="86" rx="40" fill="var(--silver)"/></svg>
      <span>SILVER</span>
    </div>
    <p class="tier-services short">PreSoak <span class="bullet">●</span> Undercarriage rinse<br><span class="bullet">●</span> Soap and Scrub <span class="bullet">●</span> Tire Shine</p>
    <div class="tier-price">
      <svg width="216" height="140"><path d="M216 40 V130 Q214 100 182 94 V40 Z" fill="var(--silver-fold)"/><rect x="0" y="0" width="216" height="86" rx="40" fill="var(--silver)"/></svg>
      <span>$85</span>
    </div>
  </section>

  <section class="tier" style="top:974px">
    <div class="tier-label">
      <svg width="216" height="140"><path d="M0 40 V130 Q2 100 34 94 V40 Z" fill="var(--express-fold)"/><rect x="0" y="0" width="216" height="86" rx="40" fill="var(--express)"/></svg>
      <span>EXPRESS</span>
    </div>
    <p class="tier-services short">PreSoak <span class="bullet">●</span> Undercarriage rinse<br><span class="bullet">●</span> Soap and Scrub</p>
    <div class="tier-price">
      <svg width="216" height="140"><path d="M216 40 V130 Q214 100 182 94 V40 Z" fill="var(--express-fold)"/><rect x="0" y="0" width="216" height="86" rx="40" fill="var(--express)"/></svg>
      <span>$75</span>
    </div>
  </section>

  <p class="contact-note">FOR MORE OPTIONS PLEASE SEE FRONT DESK<br>OFFICE: 503-555-0147</p>
</main>
</body>
</html>
```